Real Estate Business card design

Company Name: Thornbury Holdings, LLC
subtitle: We pay cash for houses!
Martin Calloway
Managing Director
518-674-2913
Mart@ThornburyHoldingsLLC.example
www.ThornburyHoldingsLLC.example

We pay referral fees for Seller and Buyer leads.

Back:
We offer referral fees for Seller and Buyer leads that close.

Please contact Ned at 518-674-2913 with your referrals or to learn more about the referral program!

I am open to different color options but I am going for a classic, elegant, clean, and professional look. Please use logo as a reference.

Target Market(s)

People selling their homes and people in the market for buying homes.

Contact Information for Business Card

please see project description

Font styles to use
Serif
Sans Serif
Script

Requirements
Must have
• must have my logo in it
Nice to have
• I like cards that are split down the middle but please come up with a few mock ups. Open to any color scheme.

```html
<!DOCTYPE html>
<html lang="en">
<head>
<meta charset="utf-8">
<title>Thornbury Holdings, LLC — Business Card</title>
<link href="https://fonts.googleapis.com/css2?family=Lato:ital,wght@0,400;0,700;1,400&display=swap" rel="stylesheet">
<style>
  :root {
    --backdrop: #e4e4e4;
    --paper: #f5f5f3;
    --slate: #434c5a;
    --slate-text: #3a404a;
    --gold: #c9a16e;
    --light-text: #eef0f2;
  }
  * { margin: 0; padding: 0; box-sizing: border-box; }
  html, body {
    width: 1200px; height: 900px; overflow: hidden;
    background: var(--backdrop);
    font-family: "Lato", Arial, sans-serif;
  }
  .canvas { position: relative; width: 1200px; height: 900px; }
  .card {
    position: absolute; left: 349px; width: 510px; height: 290px;
    text-align: center; overflow: hidden;
  }
  .card--front { top: 122px; background: var(--paper); color: var(--slate-text); }
  .card--back { top: 478px; background: var(--slate); color: var(--light-text); }

  .brand {
    position: absolute; left: 0; right: 0;
    display: flex; justify-content: center; align-items: center; gap: 8px;
    font-weight: 700; letter-spacing: 0.3px;
  }
  .brand-mark { width: 10px; height: 10px; background: var(--gold); }
  .card--front .brand { top: 64px; font-size: 20px; color: var(--slate); }
  .card--back .brand { top: 110px; font-size: 22px; color: #ffffff; }

  .tagline { position: absolute; left: 0; right: 0; top: 89px; font-style: italic; font-size: 12.5px; }
  .person-name { position: absolute; left: 0; right: 0; top: 124px; font-size: 17px; color: var(--gold); letter-spacing: 0.4px; }
  .person-phone { position: absolute; left: 0; right: 0; top: 148px; font-size: 14px; font-weight: 700; letter-spacing: 1px; }
  .contact-lines { position: absolute; left: 0; right: 0; top: 190px; font-size: 12.5px; line-height: 20px; letter-spacing: 0.2px; }

  .referral-band {
    position: absolute; left: 0; right: 0; bottom: 0; height: 47px;
    background: var(--slate); color: var(--light-text);
    font-style: italic; font-size: 12px; line-height: 47px; letter-spacing: 0.2px;
  }

  .back-offer { position: absolute; left: 0; right: 0; top: 175px; font-style: italic; font-size: 12px; letter-spacing: 0.2px; }
  .back-contact { position: absolute; left: 0; right: 0; top: 210px; font-size: 12px; line-height: 19px; letter-spacing: 0.2px; }
  .highlight { color: var(--gold); }
</style>
</head>
<body>
<main class="canvas">
  <section class="card card--front" aria-label="Business card front">
    <div class="brand"><span class="brand-mark"></span><span>Thornbury Holdings, LLC</span></div>
    <p class="tagline">We pay cash for houses!</p>
    <p class="person-name">Martin Calloway</p>
    <p class="person-phone">518-674-2913</p>
    <p class="contact-lines">Mart@ThornburyHoldingsLLC.example<br>www.ThornburyHoldingsLLC.example</p>
    <p class="referral-band">We pay referral fees for Seller and Buyer leads</p>
  </section>

  <section class="card card--back" aria-label="Business card back">
    <div class="brand"><span class="brand-mark"></span><span>Thornbury Holdings, LLC</span></div>
    <p class="back-offer">We offer referral fees for Seller and Buyer leads that close.</p>
    <p class="back-contact">Please contact <span class="highlight">Ned</span> at <span class="highlight">518-674-2913</span> with your referrals<br>or to learn more about the referral program!</p>
  </section>
</main>
</body>
</html>
```